Bref créative
Modern Business Card for Computer Service Company
Brightwave Tech Partners, Inc.
Professional
Marcus T. Hollings
Technology Engineer
4195 Larkin Avenue
Hollywood FL 33024
marcus@btp-helpdesk.com
www.btp-helpdesk.com
I would like a blurb that says "Supporting South Florida Small Business"

```html
<!DOCTYPE html>
<html lang="en">
<head>
<meta charset="utf-8">
<title>Brightwave Tech Partners, Inc. — Business Card</title>
<link rel="stylesheet" href="https://fonts.googleapis.com/css2?family=Open+Sans:wght@400;600;700&display=swap">
<style>
  :root {
    --backdrop: #e9ebee;
    --card: #ffffff;
    --navy: #1f4e96;
    --blue: #2a6fc4;
    --sky: #4fa3e0;
    --green: #6cbf2f;
    --lime: #9fd14a;
    --ink: #3a4a63;
    --muted: #6b7890;
  }
  * { box-sizing: border-box; margin: 0; padding: 0; }
  html, body { width: 1200px; height: 629px; overflow: hidden; }
  body {
    background: var(--backdrop);
    font-family: "Open Sans", Arial, sans-serif;
    color: var(--ink);
    position: relative;
  }
  .card {
    position: absolute;
    top: 166px;
    width: 520px;
    height: 297px;
    background: var(--card);
    box-shadow: 0 6px 18px rgba(20, 35, 60, 0.18);
    overflow: hidden;
  }
  .card--front { left: 50px; }
  .card--back { left: 630px; }

  .brand {
    display: flex;
    align-items: center;
    gap: 10px;
  }
  .brand__mark {
    width: 22px;
    height: 22px;
    background: var(--blue);
    flex: none;
  }
  .brand__name {
    font-weight: 700;
    color: var(--navy);
    font-size: 19px;
    line-height: 1.2;
    white-space: nowrap;
  }

  .front__lockup {
    position: absolute;
    left: 0; right: 0; top: 0; bottom: 0;
    display: flex;
    flex-direction: column;
    align-items: center;
    justify-content: center;
    gap: 12px;
  }
  .tagline {
    font-size: 11.5px;
    font-weight: 600;
    color: var(--green);
    letter-spacing: 0.06em;
    text-transform: uppercase;
    white-space: nowrap;
  }

  .card--back .brand {
    position: absolute;
    left: 34px;
    top: 42px;
  }
  .card--back .brand__name { font-size: 15px; }
  .card--back .brand__mark { width: 18px; height: 18px; }

  .person {
    position: absolute;
    left: 34px;
    top: 112px;
  }
  .person__name {
    font-size: 15px;
    font-weight: 700;
    color: var(--blue);
    white-space: nowrap;
  }
  .person__title {
    font-size: 11px;
    color: var(--muted);
    margin-top: 2px;
  }
  .person__address {
    font-size: 10.5px;
    color: var(--ink);
    margin-top: 14px;
    line-height: 1.5;
  }

  .contacts {
    position: absolute;
    left: 300px;
    top: 100px;
    list-style: none;
  }
  .contacts li {
    display: flex;
    align-items: center;
    gap: 8px;
    font-size: 10.5px;
    color: var(--ink);
    height: 19px;
    white-space: nowrap;
  }
  .contacts svg { width: 13px; height: 13px; flex: none; }

  .swoosh {
    position: absolute;
    left: 0;
    bottom: 0;
    width: 520px;
    height: 90px;
  }
</style>
</head>
<body>
  <section class="card card--front" aria-label="Card front">
    <div class="front__lockup">
      <div class="brand">
        <span class="brand__mark"></span>
        <span class="brand__name">Brightwave Tech Partners, Inc.</span>
      </div>
      <p class="tagline">Supporting South Florida Small Business</p>
    </div>
  </section>

  <section class="card card--back" aria-label="Card back">
    <div class="brand">
      <span class="brand__mark"></span>
      <span class="brand__name">Brightwave Tech Partners, Inc.</span>
    </div>

    <div class="person">
      <p class="person__name">Marcus T. Hollings</p>
      <p class="person__title">Technology Engineer</p>
      <p class="person__address">4195 Larkin Avenue<br>Hollywood FL 33024</p>
    </div>

    <ul class="contacts">
      <li>
        <svg viewBox="0 0 14 14"><circle cx="7" cy="7" r="7" fill="var(--blue)"/><path d="M4.3 3.6l1.4-.3.8 1.8-.9.7a5 5 0 0 0 2.6 2.6l.7-.9 1.8.8-.3 1.4c-3.3.3-6.4-2.8-6.1-6.1z" fill="#fff"/></svg>
        954-555-0142
      </li>
      <li>
        <svg viewBox="0 0 14 14"><circle cx="7" cy="7" r="7" fill="var(--blue)"/><rect x="4" y="5" width="6" height="4.5" fill="#fff"/><rect x="5" y="3.3" width="4" height="2" fill="#fff"/></svg>
        954-555-0187
      </li>
      <li>
        <svg viewBox="0 0 14 14"><circle cx="7" cy="7" r="7" fill="var(--blue)"/><circle cx="7" cy="7" r="3.6" fill="none" stroke="#fff" stroke-width="1"/><path d="M3.4 7h7.2M7 3.4c-1.6 2-1.6 5.2 0 7.2M7 3.4c1.6 2 1.6 5.2 0 7.2" fill="none" stroke="#fff" stroke-width=".8"/></svg>
        www.btp-helpdesk.com
      </li>
      <li>
        <svg viewBox="0 0 14 14"><circle cx="7" cy="7" r="7" fill="var(--blue)"/><rect x="3.6" y="4.6" width="6.8" height="4.8" fill="#fff"/><path d="M3.6 4.6l3.4 2.7 3.4-2.7" fill="none" stroke="var(--blue)" stroke-width=".8"/></svg>
        marcus@btp-helpdesk.com
      </li>
    </ul>

    <svg class="swoosh" viewBox="0 0 520 90" preserveAspectRatio="none" aria-hidden="true">
      <defs>
        <linearGradient id="blueBand" x1="0" x2="1" y1="0" y2="0">
          <stop offset="0" stop-color="var(--navy)"/>
          <stop offset="1" stop-color="var(--sky)"/>
        </linearGradient>
        <linearGradient id="greenBand" x1="0" x2="1" y1="0" y2="0">
          <stop offset="0" stop-color="var(--lime)"/>
          <stop offset="1" stop-color="var(--green)"/>
        </linearGradient>
      </defs>
      <path d="M0 40 C150 78 330 72 520 14 L520 50 C340 92 160 94 0 66 Z" fill="url(#greenBand)"/>
      <path d="M0 60 C170 92 350 86 520 34 L520 90 L0 90 Z" fill="url(#blueBand)"/>
      <path d="M0 72 C180 96 360 92 520 54" fill="none" stroke="#fff" stroke-width="2" opacity=".7"/>
    </svg>
  </section>
</body>
</html>
```